Bouncy castle rental needs a car wrap design

We are a young startup that rents out bouncy castles. We live in Crailsheim and have the following vehicles:
- Vornik Astra Q 2024 in white
- Car trailer
We have already had logo files created through a competition. These files are all attached.
Our website: https://fantorix-welbach.de
We would like a partial foiling, with the logo and other elements from the logo files adapted - feel free to be creative! :-) You can/may also use images from the homepage, for example. However, we are not sure how bouncy castles should be depicted on the car...
The design should be striking, young, lively and convey the theme of bouncy castles :-)
You will receive the following information as files:
- Zip file with some logo design files
- a photo of the Vornik Astra Q 2024
- A photo of the car trailer. Here are the dimensions:
- Side: 250cm x 153cm
- Front/back: 150cm x153cm
#Additional Information:
Colors frequently used on website:
Yellow: #fbd604
Yellow: #d41370
Also added our logo with white border, that it can be used on color and not just white

```html
<!DOCTYPE html>
<html lang="de">
<head>
<meta charset="utf-8">
<title>Fantorix Welbach – Anhänger-Beklebung</title>
<link href="https://fonts.googleapis.com/css2?family=Gochi+Hand&family=Oswald:wght@500;700&display=swap" rel="stylesheet">
<style>
  :root {
    --paper: #ffffff;
    --backdrop: #eef0f2;
    --ink: #111111;
    --pink: #e8336d;
    --magenta: #d41370;
    --lime: #8cc63f;
    --grass: #b3c934;
    --purple: #5b2a86;
    --teal: #56bfc6;
    --yellow: #fbd604;
    --orange: #ea6a1e;
    --coral: #e84a5f;
  }
  * { margin: 0; padding: 0; box-sizing: border-box; }
  html, body { width: 1200px; height: 728px; overflow: hidden; }
  body { background: var(--backdrop); position: relative; font-family: "Gochi Hand", cursive; color: var(--ink); }

  .panel { position: absolute; top: 156px; height: 416px; background: var(--paper); overflow: hidden; box-shadow: 0 6px 18px rgba(0,0,0,.12); }
  .panel-side { left: 41px; width: 680px; }
  .panel-front { left: 751px; width: 408px; background: var(--grass); }
  .panel svg.art { position: absolute; inset: 0; width: 100%; height: 100%; }

  .headline { position: absolute; text-transform: uppercase; line-height: 1; white-space: nowrap; }
  .headline span { display: block; }
  .panel-side .headline { left: 34px; top: 104px; font-size: 32px; }
  .panel-side .headline .l1 { color: var(--pink); }
  .panel-side .headline .l2 { color: var(--lime); }
  .panel-side .headline .l3 { color: var(--ink); }
  .panel-front .headline { left: 24px; top: 40px; font-size: 32px; }
  .panel-front .headline .l1 { color: var(--magenta); }
  .panel-front .headline .l2 { color: var(--purple); }
  .panel-front .headline .l3 { color: var(--paper); }

  .brand { position: absolute; text-align: center; }
  .brand .badge { display: block; margin: 0 auto 8px; border-radius: 50%; background: var(--yellow); }
  .brand .name { display: block; text-transform: uppercase; color: var(--ink); line-height: 1; white-space: nowrap; }
  .panel-side .brand { left: 340px; top: 36px; width: 290px; }
  .panel-side .brand .badge { width: 120px; height: 120px; }
  .panel-side .brand .name { font-size: 34px; }
  .panel-front .brand { left: 284px; top: 232px; width: 116px; }
  .panel-front .brand .badge { width: 52px; height: 52px; }
  .panel-front .brand .name { font-size: 17px; }

  .contact { position: absolute; }
  .contact .company { display: block; font-size: 22px; text-transform: uppercase; line-height: 1; white-space: nowrap; }
  .contact .web { display: block; font-family: "Oswald", sans-serif; font-weight: 500; font-size: 11px; letter-spacing: .5px; margin-top: 3px; }
  .panel-side .contact { left: 34px; top: 340px; }
  .panel-front .contact { right: 18px; bottom: 22px; text-align: right; }
  .panel-front .contact .company { font-size: 18px; }
  .panel-front .contact .web { font-size: 10px; }
</style>
</head>
<body>

<section class="panel panel-side" aria-label="Seitenansicht Anhänger">
  <svg class="art" viewBox="0 0 680 416">
    <defs>
      <linearGradient id="sunset" x1="0" x2="1" y1="0" y2="0">
        <stop offset="0" stop-color="#f3e21a"/>
        <stop offset="1" stop-color="#ea6a1e"/>
      </linearGradient>
      <linearGradient id="castleMist" x1="0" x2="0" y1="0" y2="1">
        <stop offset="0" stop-color="#f6c9cf"/>
        <stop offset="1" stop-color="#d9eef0"/>
      </linearGradient>
      <radialGradient id="photoGreen" cx=".5" cy=".5" r=".6">
        <stop offset="0" stop-color="#9fd36a"/>
        <stop offset="1" stop-color="#3f8f5a"/>
      </radialGradient>
      <radialGradient id="photoBrown" cx=".5" cy=".5" r=".6">
        <stop offset="0" stop-color="#c9a04a"/>
        <stop offset="1" stop-color="#6b4a2a"/>
      </radialGradient>
      <radialGradient id="photoJungle" cx=".5" cy=".5" r=".6">
        <stop offset="0" stop-color="#d6e35a"/>
        <stop offset="1" stop-color="#5ea94a"/>
      </radialGradient>
    </defs>
    <path class="blob-sunset" d="M0 0 H232 C214 52 180 82 132 74 C88 66 44 58 0 84 Z" fill="url(#sunset)"/>
    <path class="blob-green" d="M244 0 H470 C420 4 370 22 334 46 C300 70 270 84 200 78 C228 60 242 34 244 0 Z" fill="var(--lime)"/>
    <path class="swoosh-teal" d="M0 92 C40 62 110 54 160 80 C220 112 232 200 272 252 C322 312 420 300 500 312 C582 322 652 332 662 372 C666 396 640 404 600 404 L420 404 C330 404 298 382 258 350 C210 310 208 220 178 162 C150 112 100 92 40 102 C20 105 8 110 0 114 Z" fill="var(--teal)"/>
    <rect class="castle-fade" x="20" y="220" width="190" height="170" rx="12" fill="url(#castleMist)" opacity=".4" role="img" aria-label="Blasse Hüpfburg-Illustration mit Stadtsilhouette im Hintergrund"/>
    <circle cx="281" cy="247" r="48" fill="url(#photoGreen)" stroke="#111" stroke-width="2" role="img" aria-label="Foto einer grünen Hüpfburg"/>
    <circle cx="421" cy="291" r="53" fill="url(#photoBrown)" stroke="#111" stroke-width="2" role="img" aria-label="Foto einer Dschungel-Hüpfburg mit Rutsche"/>
    <circle cx="564" cy="333" r="58" fill="url(#photoJungle)" stroke="#111" stroke-width="2" role="img" aria-label="Foto einer Tier-Hüpfburg mit Rutsche"/>
  </svg>

  <h2 class="headline"><span class="l1">Neu seit</span><span class="l2">April 2024</span><span class="l3">in Crailsheim</span></h2>

  <div class="brand">
    <span class="badge"></span>
    <span class="name">Fantorix Welbach</span>
  </div>

  <p class="contact"><span class="company">Fantorix Welbach</span><span class="web">www.fantorix-welbach.de</span></p>
</section>

<section class="panel panel-front" aria-label="Frontansicht Anhänger">
  <svg class="art" viewBox="0 0 408 416">
    <defs>
      <linearGradient id="mistFront" x1="0" x2="0" y1="0" y2="1">
        <stop offset="0" stop-color="#f3f0d0"/>
        <stop offset="1" stop-color="#cfe9ec"/>
      </linearGradient>
    </defs>
    <path class="swoosh-teal" d="M0 342 C70 282 130 232 190 212 C260 190 340 182 408 194 V416 H0 Z" fill="var(--teal)"/>
    <path class="field-white" d="M90 416 C110 345 160 288 220 258 C280 232 345 224 408 232 V416 Z" fill="var(--paper)"/>
    <path class="line-red" d="M0 332 C70 272 130 222 190 202 C260 180 340 172 408 184" fill="none" stroke="var(--coral)" stroke-width="7"/>
    <rect class="castle-fade" x="10" y="270" width="100" height="120" rx="10" fill="url(#mistFront)" opacity=".35" role="img" aria-label="Blasse Hüpfburg-Illustration im Hintergrund"/>
  </svg>

  <h2 class="headline"><span class="l1">Neu seit</span><span class="l2">April 2024</span><span class="l3">in Crailsheim</span></h2>

  <div class="brand">
    <span class="badge"></span>
    <span class="name">Fantorix<br>Welbach</span>
  </div>

  <p class="contact"><span class="company">Fantorix Welbach</span><span class="web">www.fantorix-welbach.de</span></p>
</section>

</body>
</html>
```